【 概要 】 ホームページのTOP画像のデザインを募集いたします。 飲食店専用ホームページ制作です。 メインターゲットは飲食店オーナーの方々です。 飲食のホームページにあった「どんなお店なのか」、「どんなメニュ・どんなコースがあるか」など、 そのお店を気になった方々に来店を促すようなTOP画像が希望です。 【 依頼内容 】 ・サイズ:1920px×1080px ・作成数: 1種類 ・利用用途:ホームページトップ画像 ・色:オレンジ/赤/黄色 ・文言:あなたのお店をオリジナルデザインで作ってみませんか? 【 デザインイメージ 】 ・雰囲気:信頼感、安心感があり、ポップ感 ・現在制作途中のホームページにあった感じ http://sampwebnoren.com/ ・参考他社デザイン https://www.hanamuraya.co.jp/menu/kikaku/ また飲食以外も対象にしたいと思ったので別案も制作していただけたら幸いです。 【 依頼内容 】 色:グレー/白/黒 文言:ホームページはオリジナルデザインで! 参考URL:https://qv-webworks.jp/hp/?utm_source=kensaku&utm_medium=cpc&qclid=QRS.2004815367.PXbTwLcdFhZNruqk5p8w27AKRGetSd3hvm-qWFBCZjBXFgKQ5_E_CzX 【 契約金額(税抜) 】 1万円 ※契約金額(税込)からシステム利用料を差し引いた金額が、ワーカーさまの受取金額となります その他ご質問等ありましたら、気軽にお問い合わせください。 ご応募をお待ちしております! |
| https://www.hanamuraya.co.jp/menu/kikaku/ | ||
私共の内容をよく理解していただいた上で作成していただきありがとうございます。
今回korunote様のご提案が弊社のHPの表画面での使用に一番最適だと考え作用させていただきます。
皆様色々ご提案ありがとうございます。とても素敵なデザインを見していただきました。
弊社は今後よくご依頼などをさせていただきますので、その際は皆様また力を貸していただければと思います。

```html
<!DOCTYPE html>
<html lang="ja">
<head>
<meta charset="UTF-8">
<title>飲食店ホームページ制作 トップビジュアル</title>
<link rel="stylesheet" href="https://fonts.googleapis.com/css2?family=M+PLUS+Rounded+1c:wght@700;800;900&family=Space+Mono&display=swap">
<style>
  :root {
    --yellow-light: #fae7a0;
    --yellow: #f7cf52;
    --yellow-deep: #f2b82e;
    --accent-yellow: #ffe34d;
    --magenta: #b5145a;
    --magenta-dark: #9c0f4c;
    --ink: #1c1a1a;
    --white: #ffffff;
  }
  * { box-sizing: border-box; margin: 0; padding: 0; }
  html, body { width: 1200px; height: 674px; overflow: hidden; }
  body {
    position: relative;
    background: linear-gradient(180deg, var(--yellow-light) 0%, var(--yellow) 50%, var(--yellow-deep) 100%);
    font-family: "M PLUS Rounded 1c", sans-serif;
    color: var(--ink);
  }
  .ingredients-scatter {
    position: absolute; inset: 0;
    background:
      radial-gradient(ellipse 200px 320px at 30px 260px, rgba(120,150,70,.55), rgba(120,150,70,0) 70%),
      radial-gradient(ellipse 220px 140px at 1150px 90px, rgba(150,160,80,.45), rgba(150,160,80,0) 70%),
      radial-gradient(ellipse 520px 120px at 600px 10px, rgba(214,160,90,.45), rgba(214,160,90,0) 75%),
      radial-gradient(ellipse 180px 120px at 1140px 250px, rgba(230,180,90,.4), rgba(230,180,90,0) 70%);
  }
  .frame {
    position: absolute; left: 112px; top: 52px; width: 990px; height: 560px;
    background: var(--magenta);
    border-radius: 6px;
  }
  .photo { position: absolute; }
  .photo--meat     { left: 124px; top: 64px;  width: 316px; height: 126px; background: linear-gradient(135deg, #a9b27a, #e3b9a6 60%, #efd3c4); }
  .photo--pasta    { left: 448px; top: 64px;  width: 322px; height: 126px; background: linear-gradient(135deg, #c9b190, #efd9a8 55%, #e2c58f); }
  .photo--rice     { left: 778px; top: 64px;  width: 312px; height: 126px; background: linear-gradient(135deg, #b4856a, #e6a46a 50%, #efcf8c); }
  .photo--bibimbap { left: 124px; top: 456px; width: 316px; height: 144px; background: linear-gradient(135deg, #b88e73, #d99a6c 50%, #e8b57f); }
  .photo--tart     { left: 448px; top: 456px; width: 322px; height: 144px; background: linear-gradient(135deg, #efdcc6, #db8a8e 55%, #c9656e); }
  .photo--pizza    { left: 778px; top: 456px; width: 312px; height: 144px; background: linear-gradient(135deg, #f0d9a0, #e8a274 50%, #f4e6c0); }
  .message-panel {
    position: absolute; left: 124px; top: 190px; width: 966px; height: 266px;
    background: var(--white);
  }
  .lead-pill {
    position: absolute; left: 262px; top: 176px; width: 440px; height: 60px;
    background: var(--magenta-dark);
    border-radius: 4px;
    color: var(--accent-yellow);
    font-weight: 800; font-size: 29px; letter-spacing: 1px;
    display: flex; align-items: center; justify-content: center;
  }
  .ticks { position: absolute; left: 296px; top: 246px; }
  .headline {
    position: absolute; left: 282px; top: 274px;
    font-weight: 900; font-size: 70px; line-height: 1; letter-spacing: 2px;
    white-space: nowrap;
  }
  .headline small { font-size: 38px; letter-spacing: 0; }
  .headline-rule {
    position: absolute; left: 284px; top: 364px; width: 604px; height: 5px;
    background: var(--accent-yellow);
  }
  .subline {
    position: absolute; left: 340px; top: 400px;
    font-weight: 800; font-size: 38px; line-height: 1.2; letter-spacing: 5px;
  }
  .badge {
    position: absolute; left: 942px; top: 432px; width: 148px; height: 148px;
    border-radius: 50%;
    background: var(--accent-yellow);
    border: 5px solid var(--magenta);
    color: var(--magenta);
    font-weight: 900; font-size: 24px; line-height: 1.3;
    display: flex; align-items: center; justify-content: center; text-align: center;
  }
  .tagline {
    position: absolute; left: 0; width: 1200px; top: 620px;
    text-align: center;
    font-family: "Space Mono", monospace;
    font-size: 20px; letter-spacing: 10px; word-spacing: 18px;
    color: var(--ink);
  }
</style>
</head>
<body>
  <div class="ingredients-scatter" role="img" aria-label="野菜・きのこ・ナッツなど色とりどりの食材が周囲に散らばる写真"></div>

  <div class="frame"></div>
  <div class="photo photo--meat" role="img" aria-label="焼肉用の豚肉とサンチュ・ナムルの写真"></div>
  <div class="photo photo--pasta" role="img" aria-label="クリームパスタの写真"></div>
  <div class="photo photo--rice" role="img" aria-label="ねぎと唐辛子をのせた丼の写真"></div>
  <div class="photo photo--bibimbap" role="img" aria-label="石焼ビビンバとステーキの写真"></div>
  <div class="photo photo--tart" role="img" aria-label="ベリーのタルトの写真"></div>
  <div class="photo photo--pizza" role="img" aria-label="マルゲリータピザの写真"></div>

  <div class="message-panel"></div>
  <div class="lead-pill">あなたのお店のホームページを</div>

  <svg class="ticks" width="300" height="22" viewBox="0 0 300 22" aria-hidden="true">
    <g fill="none" stroke="#ffe34d" stroke-width="4" stroke-linecap="round" stroke-linejoin="round">
      <path d="M4 10 L10 17 L22 3"/>
      <path d="M62 10 L68 17 L80 3"/>
      <path d="M126 10 L132 17 L144 3"/>
      <path d="M188 10 L194 17 L206 3"/>
      <path d="M252 10 L258 17 L270 3"/>
    </g>
  </svg>
  <div class="headline">オリジナルデザイン<small>で</small></div>
  <div class="headline-rule"></div>
  <div class="subline">作ってみませんか？</div>

  <div class="badge">飲食店<br>オーナー様<br>注目!</div>

  <div class="tagline">Original design presents</div>
</body>
</html>
```